I make small projects usually ranging from cutting boards, kitchen utensils , cedar gardens projects, basically anything I can fit in a 2 car garage workshop. I've been ask by numerous people if I have website or a facebook page or something where they go look at my products/abilities. I pretty much make anything anyone wants out of wood and can customize to their needs.

R.T.Belcourt Custom Woodworks Inc. is my business name.

At this time I'm currently seeking a branding logo and business card set for my new business. I'm based out of the city of Edmonton, Alberta, Canada. My target market would be Middle class to upper class, new home-owners who like quality products to compliment the look of their new homes and property at decent prices. Although this my current work practice I am thinking I venture into finish carpentry long term and that is why I choose the name to be more formal. However I would the design to different that just a plain card. Would like to incorporate wood grain color or pattern. I would like a slogan or logo text, but I have no idea what ill leave that up to you and see what you come back with.

Target Market(s)

My target market would be Middle class to upper class, new home-owners who like quality products to compliment the look of their new homes and property at decent prices.

Industry/Entity Type

Carpentry

Contact Information for Business Card

Rowan T. Belcourt
Craftsmen

R.T.Belcourt Custom Woodworks Inc
Address: 2817 Thornbury Way SW, Edmonton, A.B., T5K 2P8
Cell: (780) 555-0193
Smtp: rtbwoodworks@examplemail.net
Website: XXXXXXX yet to be determined
Facebook: R.T.Belcourt Custom Woodworks Inc.

Logo styles of interest
Emblem Logo
Pictorial/Combination Logo
Abstract Logo
Lettermark Logo
Requirements
Nice to have
• Although there is a allot information in the business card detail area, feel free to alter as you see fir. example: remove business address, website(as i dont have one yet)

```html
<!DOCTYPE html>
<html lang="en">
<head>
<meta charset="utf-8">
<title>R.T. Belcourt Custom Woodworks – Stationery Set</title>
<link rel="stylesheet" href="https://fonts.googleapis.com/css2?family=Cinzel:wght@400&family=Open+Sans:wght@400;600&display=swap">
<style>
  :root {
    --backdrop: #2b160a;
    --wood-dark: #3d1e0b;
    --wood-mid: #6a3512;
    --wood-warm: #8a4a1c;
    --paper: #ffffff;
    --ink-light: #ffffff;
    --ink-dark: #2a2a2a;
    --footer-band: #3b1a0c;
  }
  * { margin: 0; padding: 0; box-sizing: border-box; }
  html, body { width: 1200px; height: 1000px; overflow: hidden; }
  body {
    position: relative;
    background: var(--backdrop);
    font-family: "Open Sans", Arial, sans-serif;
    color: var(--ink-light);
  }

  .wordmark {
    font-family: "Open Sans", Arial, sans-serif;
    font-weight: 400;
    color: var(--ink-light);
    text-transform: uppercase;
    white-space: nowrap;
  }
  .wordmark .name { display: block; line-height: 1; letter-spacing: 0.04em; }
  .wordmark .trade { display: block; letter-spacing: 0.24em; margin-top: 0.45em; line-height: 1; }

  .brand-lockup { position: absolute; left: 66px; top: 98px; }
  .brand-lockup .name { font-size: 50px; }
  .brand-lockup .trade { font-size: 19px; }

  .wood-surface { background: linear-gradient(160deg, var(--wood-warm) 0%, var(--wood-mid) 45%, var(--wood-dark) 100%); }

  .letterhead {
    position: absolute; left: 560px; top: 110px;
    width: 590px; height: 764px;
    background: var(--paper);
    box-shadow: 0 12px 30px rgba(0,0,0,0.45);
  }
  .letterhead-header { height: 92px; padding: 26px 0 0 30px; }
  .letterhead-header .name { font-size: 24px; }
  .letterhead-header .trade { font-size: 9.5px; }
  .letterhead-contact {
    position: absolute; left: 30px; bottom: 40px;
    color: var(--ink-dark);
  }
  .letterhead-footer { position: absolute; left: 0; right: 0; bottom: 0; height: 12px; background: var(--footer-band); }

  .card {
    position: absolute; width: 330px; height: 189px;
    box-shadow: 0 10px 24px rgba(0,0,0,0.5);
  }
  .card-front { left: 180px; top: 300px; display: flex; align-items: center; justify-content: center; }
  .card-front .name { font-size: 30px; }
  .card-front .trade { font-size: 11.5px; }
  .card-back { left: 160px; top: 540px; padding: 22px 26px; }

  .holder-name {
    font-family: "Cinzel", "Times New Roman", serif; font-size: 18px; font-weight: 400;
    padding-bottom: 8px; border-bottom: 1px solid var(--ink-light); width: 270px;
    white-space: nowrap;
  }
  .contact-list { list-style: none; }
  .contact-list li { display: flex; gap: 8px; white-space: nowrap; }
  .contact-list .label { font-weight: 600; width: 12px; }
  .card-back .contact-list { margin-top: 16px; font-size: 13px; line-height: 1.5; }
  .card-back .contact-list .email { font-size: 11.5px; }
  .card-back .address { margin-top: 12px; font-size: 11px; white-space: nowrap; }
  .letterhead-contact .contact-list { font-size: 11px; line-height: 1.45; }
  .letterhead-contact .contact-list .email { font-size: 9.5px; }
  .letterhead-contact .address { margin-top: 10px; font-size: 9.5px; white-space: nowrap; }
</style>
</head>
<body>
  <div class="brand-lockup wordmark">
    <span class="name">R.T. Belcourt</span>
    <span class="trade">Custom Woodworks</span>
  </div>

  <section class="letterhead">
    <header class="letterhead-header wood-surface wordmark" role="img" aria-label="Wood grain band with company name">
      <span class="name">R.T. Belcourt</span>
      <span class="trade">Custom Woodworks</span>
    </header>
    <div class="letterhead-contact">
      <ul class="contact-list">
        <li><span class="label">O</span><span>(780) 555-0147</span></li>
        <li><span class="label">M</span><span>(780) 555-0193</span></li>
        <li><span class="label">E</span><span class="email">rtbwoodworks@examplemail.net</span></li>
      </ul>
      <p class="address">2817 Thornbury Way SW, Edmonton, AB T5K 2P8</p>
    </div>
    <div class="letterhead-footer"></div>
  </section>

  <section class="card card-front wood-surface" role="img" aria-label="Wood grain business card front with company name">
    <div class="wordmark">
      <span class="name">R.T. Belcourt</span>
      <span class="trade">Custom Woodworks</span>
    </div>
  </section>

  <section class="card card-back wood-surface" aria-label="Wood grain business card back">
    <h2 class="holder-name">Rowan T. Belcourt</h2>
    <ul class="contact-list">
      <li><span class="label">O</span><span>(780) 555-0147</span></li>
      <li><span class="label">M</span><span>(780) 555-0193</span></li>
      <li><span class="label">E</span><span class="email">rtbwoodworks@examplemail.net</span></li>
    </ul>
    <p class="address">2817 Thornbury Way SW, Edmonton, AB T5K 2P8</p>
  </section>
</body>
</html>
```